Brindle Press Promotional Brochure

www.brindlepress-demo.com

Award Winning Trade Printer

Refer to website and create a Brochure 5 colour using metallic gold 871
Images can be supplied hi resolution from website if required or further images

Using the following titles
Specialising in High Quality Trade Printing Nationally
Books, Catalogues, Booklets
Brochures, Flyers and Mail Outs
Presentation Folders
Business Cards and Stationery
Also Specialising in
Labels and Packaging
print and engineering from original concept packaging

Come and see our friendly staff or visit our website
Compare our prices via email

Target Market(s)

Print Buyers

Industry/Entity Type

Printing

Requirements
Must have
• a pms Gold included in final artwork
• A Premium/Quality/upmarket approach
• Hi Quality IMAGES etc.
• I placed an image of an awards dinner BUT that is just there for a personal image not essential to have by any means
Nice to have
• Sections in the brochure for each type of print or panel with a cover page wow!!! BRINDLE!
Should not have
• poor quality images

```html
<!DOCTYPE html>
<html lang="en">
<head>
<meta charset="utf-8">
<title>Brindle Press – Inner Spread</title>
<link rel="stylesheet" href="https://fonts.googleapis.com/css2?family=Cinzel:wght@500;600&family=Questrial&display=swap">
<style>
  :root {
    --gold: #d9a21b;
    --gold-light: #f0c64a;
    --accent: #e0521c;
    --ink: #1c1c1c;
    --night: #101010;
    --paper: #ffffff;
    --canvas: #d6d6d6;
  }
  * { box-sizing: border-box; margin: 0; padding: 0; }
  html, body { width: 1200px; height: 800px; overflow: hidden; background: var(--canvas); }
  .spread { position: relative; display: flex; width: 1200px; height: 800px; }
  .panel { position: relative; width: 400px; height: 800px; background: var(--paper); overflow: hidden; }
  .panel + .panel { border-left: 1px solid #e4e4e4; }
  .panel-art { position: absolute; inset: 0; width: 400px; height: 800px; }
  .panel-copy {
    position: absolute; left: 40px; right: 40px;
    font-family: "Questrial", sans-serif; font-size: 13px; line-height: 1.42;
    color: var(--ink); text-align: center;
  }
  .panel-copy p + p { margin-top: 12px; }
  .panel-heading {
    font-family: "Cinzel", serif; font-weight: 600; font-size: 25px;
    color: var(--accent); letter-spacing: 0.5px; margin-bottom: 10px; line-height: 1.1;
  }
  .quality-copy { top: 318px; }
  .about-copy { top: 262px; }
  .services-copy { top: 92px; left: 44px; right: 30px; text-align: left; }
  .services-copy .panel-heading { margin-bottom: 8px; }
  .service-list { list-style: none; }
  .service-list li { position: relative; padding-left: 26px; font-size: 14px; line-height: 1.5; }
  .service-list li::before {
    content: ""; position: absolute; left: 0; top: 4px; width: 12px; height: 12px;
    border-radius: 50%; background: radial-gradient(circle at 40% 35%, #fff7dc, var(--gold-light) 60%, var(--gold));
    border: 1px solid #c8c8c8;
  }
  .subheading {
    font-family: "Cinzel", serif; font-weight: 600; font-size: 17px;
    color: var(--accent); margin: 6px 0 4px;
  }
  .brand-tile {
    position: absolute; left: 226px; top: 688px; width: 154px; height: 46px;
    background: var(--night); display: flex; align-items: center; justify-content: center;
    font-family: "Questrial", sans-serif; font-size: 18px; letter-spacing: 7px; color: #ffffff;
  }
</style>
</head>
<body>
<main class="spread">

  <section class="panel panel-quality">
    <svg class="panel-art" viewBox="0 0 400 800" aria-hidden="false">
      <defs>
        <linearGradient id="bookTones" x1="0" y1="0" x2="1" y2="0">
          <stop offset="0" stop-color="#c8202d"/>
          <stop offset="0.2" stop-color="#e9e6e0"/>
          <stop offset="0.45" stop-color="#4a78b8"/>
          <stop offset="0.65" stop-color="#f2f0ea"/>
          <stop offset="1" stop-color="#dcd8cf"/>
        </linearGradient>
        <linearGradient id="staffTones" x1="0" y1="0" x2="1" y2="1">
          <stop offset="0" stop-color="#9aa3ad"/>
          <stop offset="1" stop-color="#3f4a5a"/>
        </linearGradient>
      </defs>
      <rect role="img" aria-label="Photograph of an open printed book with colourful die-cut pages" x="0" y="0" width="400" height="320" fill="url(#bookTones)"/>
      <path d="M0 300 C120 262 260 312 400 246 L400 800 L0 800 Z" fill="var(--paper)"/>
      <path d="M0 300 C120 262 260 312 400 246" fill="none" stroke="var(--gold)" stroke-width="16"/>
      <path d="M0 726 C140 696 280 764 400 706 L400 800 L0 800 Z" fill="var(--night)"/>
      <path d="M0 726 C140 696 280 764 400 706" fill="none" stroke="var(--gold)" stroke-width="10"/>
      <circle role="img" aria-label="Photograph of staff working at a print workstation" cx="76" cy="738" r="56" fill="url(#staffTones)" stroke="var(--gold)" stroke-width="7"/>
    </svg>
    <div class="panel-copy quality-copy">
      <h2 class="panel-heading">Quality</h2>
      <p>Brindle Press is a Tasmanian institution.</p>
      <p>With humble beginnings starting in the family home in 1978 before moving to the premises where you can find us today, Brindle Press has always been a market leader and committed to printing of the highest distinction.</p>
      <p>Strong family traditions have conveyed particular Brindle printing skills and craftsmanship through the decades including complex tricks of the trade that are learnt, practiced and refined in-house to build a reputation of superiority and brilliance.</p>
      <p>In fact, Brindle was the first Tasmanian owned company to install a four-colour process offset Press in Tasmania back in 1992 and have a continual goal for improvement and excellence in every job done.</p>
    </div>
    <div class="brand-tile">BRINDLE</div>
  </section>

  <section class="panel panel-about">
    <svg class="panel-art" viewBox="0 0 400 800">
      <defs>
        <linearGradient id="cardTones" x1="0" y1="0" x2="1" y2="1">
          <stop offset="0" stop-color="#8f9093"/>
          <stop offset="0.45" stop-color="#1e1e1e"/>
          <stop offset="0.7" stop-color="#b3262a"/>
          <stop offset="1" stop-color="#eeeeee"/>
        </linearGradient>
        <linearGradient id="folderTones" x1="0" y1="0" x2="1" y2="1">
          <stop offset="0" stop-color="#1a1a1a"/>
          <stop offset="0.6" stop-color="#2c3a34"/>
          <stop offset="1" stop-color="#f1f1ee"/>
        </linearGradient>
      </defs>
      <rect role="img" aria-label="Photograph of a black invitation card with red foil detail" x="0" y="0" width="400" height="300" fill="url(#cardTones)"/>
      <path d="M0 250 C140 240 260 130 400 100 L400 800 L0 800 Z" fill="var(--paper)"/>
      <path d="M0 250 C140 240 260 130 400 100" fill="none" stroke="var(--gold)" stroke-width="16"/>
      <rect role="img" aria-label="Photograph of a dark presentation folder with printed booklet" x="0" y="560" width="400" height="240" fill="url(#folderTones)"/>
      <path d="M0 560 L400 560 L400 612 C280 636 160 722 0 726 Z" fill="var(--paper)"/>
      <path d="M400 612 C280 636 160 722 0 726" fill="none" stroke="var(--gold)" stroke-width="12"/>
    </svg>
    <div class="panel-copy about-copy">
      <h2 class="panel-heading">About Us</h2>
      <p>Printing is more than a job - it is an artform.</p>
      <p>Brindle Press takes great pride in our craftsmanship, skill and ingenuity to ensure we deliver the best possible printing outcome for every job.</p>
      <p>Known widely as a ‘printer’s printer’ there is no job too small, large or complex for Brindle Press from your smallest business card run through to the most intricate and difficult printing task.</p>
      <p>Renown for high quality of work, state-of-the-art technology and commitment to excellence, Brindle have worked hard to be established as one of the premier printers in Tasmania.</p>
      <p>Pride and quality drive the efforts of staff to ensure your printing requirements are delivered on-time with professionalism and expertise.</p>
    </div>
  </section>

  <section class="panel panel-services">
    <svg class="panel-art" viewBox="0 0 400 800">
      <defs>
        <linearGradient id="skyTones" x1="0" y1="0" x2="0" y2="1">
          <stop offset="0" stop-color="#eef2f6"/>
          <stop offset="0.5" stop-color="#c9d3de"/>
          <stop offset="1" stop-color="#f3f5f8"/>
        </linearGradient>
      </defs>
      <path d="M0 0 H400 V28 C280 40 120 58 0 96 Z" fill="var(--night)"/>
      <path d="M400 28 C280 40 120 58 0 96" fill="none" stroke="var(--gold)" stroke-width="12"/>
      <rect role="img" aria-label="Photograph of a falcon in flight against a pale sky" x="0" y="470" width="400" height="330" fill="url(#skyTones)"/>
      <path d="M0 470 H400 V486 C270 470 160 560 0 590 Z" fill="var(--paper)"/>
      <path d="M400 486 C270 470 160 560 0 590" fill="none" stroke="var(--gold)" stroke-width="16"/>
    </svg>
    <div class="panel-copy services-copy">
      <h2 class="panel-heading">We Are<br>Specialising In</h2>
      <ul class="service-list">
        <li>High Quality Trade Printing</li>
        <li>Nationally Books</li>
        <li>Catalogues</li>
        <li>Booklets</li>
        <li>Brochures</li>
        <li>Flyers and Mail Outs</li>
        <li>Presentation Folders</li>
        <li>Business Cards</li>
        <li>Stationery</li>
      </ul>
      <h3 class="subheading">Also Specialising In</h3>
      <ul class="service-list">
        <li>Labels and Packaging print</li>
        <li>Engineering From Original</li>
        <li>Concept Packaging</li>
      </ul>
    </div>
  </section>

</main>
</body>
</html>
```